Tidewell Oyster-new seafood raw bar restaurant menu

We are a Local Seafood & Raw Bar restaurant that is looking to open in 3 months. I need-Dinner Menu Design, Happy Hour Menu, Cocktail Menu, Brunch Menu, Lunch Menu. I'd like to have you start w/ the dinner menu first then whomever I choose will also do the rest of my menus. The SHELLHOUSE by Kelpcove menu is the direction im going for as far as font organization. Id like you to give us our own personal touch. Ive also provided a mock menu that a local designer started that can't finish due to timing.

Target Market(s)

mid to high end casual seafood restaurant

Industry/Entity Type

restaurant

Font styles to use
Serif
Sans Serif

Colors
0054AA
0677BA
7BADD7
CADEEF
E8F1F8
0094D4
00A9DD
6FCCEA
C7EBF8
E9F6FB
00AB8E
00BBA5
67D7C9
C6EFE9
E9F9F6

Requirements
Must have
• 11" x 14" size

```html
<!DOCTYPE html>
<html lang="en">
<head>
<meta charset="utf-8">
<title>Tidewell Oyster – Dinner Menu</title>
<link rel="stylesheet" href="https://fonts.googleapis.com/css2?family=Lilita+One&family=Hind:wght@300;400&display=swap">
<style>
  :root{
    --bg:#e4fbf2;
    --navy:#1a3aa6;
    --blue:#2a8ae0;
    --desc:#3396e4;
    --panel:#c2f5e1;
  }
  *{margin:0;padding:0;box-sizing:border-box}
  html,body{width:943px;height:1200px;overflow:hidden;background:var(--bg)}
  .menu{position:relative;width:943px;height:1200px;background:var(--bg);font-family:"Hind",sans-serif;color:var(--desc)}
  .rope{position:absolute;height:4px;background:repeating-linear-gradient(115deg,var(--navy) 0 2px,transparent 2px 4px)}
  .rope-v{position:absolute;width:4px;background:repeating-linear-gradient(25deg,var(--navy) 0 2px,transparent 2px 4px)}
  .brand{position:absolute;left:0;top:62px;width:943px;display:flex;justify-content:center;align-items:center;gap:22px}
  .brand-dot{width:44px;height:44px;border-radius:50%;background:var(--navy);flex:none}
  .brand-name{font-family:"Lilita One",sans-serif;font-weight:400;font-size:44px;line-height:1;letter-spacing:1px;color:var(--navy);white-space:nowrap}
  .col-title{position:absolute;font-family:"Lilita One",sans-serif;color:var(--blue);font-size:21px;letter-spacing:.5px;text-align:center;line-height:21px}
  .items{position:absolute;list-style:none}
  .item{position:relative;margin-bottom:14px}
  .items.mid .item{margin-bottom:17px}
  .name{font-family:"Lilita One",sans-serif;color:var(--navy);font-size:13.5px;line-height:21px;letter-spacing:.3px;text-transform:uppercase}
  .name .price::before{content:"|";margin:0 9px 0 7px;font-family:"Hind",sans-serif;font-weight:400}
  .desc{font-weight:300;font-size:13px;line-height:16.5px;color:var(--desc)}
  .pick{position:absolute;left:-30px;top:2px;width:17px;height:17px;border-radius:50%;background:var(--navy)}
  .chef{position:absolute;left:351px;top:287px;width:32px;height:24px;border:2px solid var(--navy);border-radius:10px 10px 3px 3px}
  .chef-name{position:absolute;left:394px;top:289px;font-family:"Lilita One",sans-serif;color:var(--navy);font-size:13.5px;line-height:16.5px;text-transform:uppercase}
  .oyster-box{position:absolute;left:347px;top:345px;width:247px;height:245px;background:var(--panel);text-align:center}
  .box-head{font-family:"Lilita One",sans-serif;font-weight:400;color:var(--navy);font-size:17px;letter-spacing:.4px}
  .box-line{font-weight:300;font-size:13px;color:var(--desc);line-height:16px}
  .box-line b{font-family:"Lilita One",sans-serif;font-weight:400;color:var(--blue)}
  .box-line .sep{margin:0 8px}
  .band{position:absolute;left:51px;top:1041px;width:839px;height:82px;background:var(--panel)}
  .band-head{position:absolute;font-family:"Lilita One",sans-serif;font-weight:400;color:var(--navy);font-size:22px;letter-spacing:.5px}
  .band-text{position:absolute;font-weight:400;font-size:13px;line-height:21px;color:var(--navy)}
  .legend{position:absolute;left:377px;top:1141px;display:flex;align-items:center;gap:16px;font-family:"Hind",sans-serif;font-weight:400;font-size:11px;color:var(--blue);letter-spacing:.3px}
  .legend .dot{width:19px;height:19px;border-radius:50%;background:var(--navy)}
</style>
</head>
<body>
<main class="menu">
  <header class="brand">
    <span class="brand-dot"></span>
    <h1 class="brand-name">TIDEWELL OYSTER</h1>
  </header>

  <span class="rope" style="left:54px;top:176px;width:835px"></span>
  <span class="rope-v" style="left:325px;top:191px;height:824px"></span>
  <span class="rope-v" style="left:616px;top:191px;height:824px"></span>

  <h2 class="col-title" style="left:54px;top:200px;width:260px">SMALLER</h2>
  <h2 class="col-title" style="left:341px;top:200px;width:260px">RAW BAR/CHILLED<br>SEAFOOD</h2>
  <h2 class="col-title" style="left:629px;top:200px;width:260px">SIGNATURES</h2>
  <span class="rope" style="left:54px;top:247px;width:260px"></span>
  <span class="rope" style="left:341px;top:263px;width:260px"></span>
  <span class="rope" style="left:629px;top:247px;width:260px"></span>

  <ul class="items" style="left:87px;top:267px;width:230px">
    <li class="item"><p class="name">Fried Shrimp<span class="price">$0</span></p><p class="desc">Remoulade</p></li>
    <li class="item"><p class="name">Mussels<span class="price">$0</span></p><p class="desc">Local bacon, shallot, garlic, tomato,<br>spicy herb butter</p></li>
    <li class="item"><p class="name">Roasted Oysters<span class="price">$0</span></p><p class="desc">½ dozen, Choice of Rockefeller,<br>Bienville, Tidewell special</p></li>
    <li class="item"><p class="name">Shrimp &amp; Grits<span class="price">$0</span></p><p class="desc">Local andouille, roasted peppers,<br>garlic, shallot, charred tomato</p></li>
    <li class="item"><p class="name">Crab Mac'n Cheese<span class="price">$0</span></p><p class="desc">Cheddar, fontina, cotija,<br>local pasta shells</p></li>
    <li class="item"><span class="pick"></span><p class="name">Shrimp Remoulade<span class="price">$0</span></p><p class="desc">Avocado, fried green tomato</p></li>
    <li class="item"><p class="name">Pumpkin Risotto<span class="price">$0</span></p><p class="desc">Herbs, dried cherry, local mushrooms</p></li>
    <li class="item"><p class="name">Caeser<span class="price">$0</span></p><p class="desc">Baby gem lettuce, parmesan</p></li>
    <li class="item"><p class="name">Greenrow Farms<br>Crisp Greens Salad<span class="price">$0</span></p><p class="desc">Fig, goat cheese, spiced pepitos,<br>sour cherry vinaigrette</p></li>
    <li class="item"><p class="name">Clam Chowder<span class="price">$0</span></p><p class="desc">New England style</p></li>
    <li class="item"><span class="pick"></span><p class="name">Baja Fish Tacos<span class="price">$0</span></p><p class="desc">Slaw, cilantro, lime</p></li>
    <li class="item"><p class="name">Steak Taco<span class="price">$0</span></p><p class="desc">Mojo, dried chili salsa, pickled onion,<br>cotija</p></li>
  </ul>

  <span class="chef" role="img" aria-label="Chef hat icon"></span>
  <p class="chef-name">Oyster Chef's<br>Preparation<span style="font-family:Hind,sans-serif;margin:0 8px">|</span>$0</p>

  <section class="oyster-box">
    <h3 class="box-head" style="margin-top:17px">OYSTER SELECTION</h3>
    <p class="box-line" style="margin-top:8px">House<span class="sep">|</span><b>$0</b><span style="margin-left:24px">East Coast</span><span class="sep">|</span><b>$0</b></p>
    <p class="box-line" style="margin-top:9px">Regional<span class="sep">|</span><b>$0</b></p>
    <p class="box-line" style="margin-top:9px">Accompaniments, top'em</p>
    <h3 class="box-head" style="margin-top:16px">SEAFOOD TOWER</h3>
    <p class="box-line" style="margin-top:3px">Small<span class="sep">|</span><b>$0</b></p>
    <p class="box-line" style="margin-top:9px">Large<span class="sep">|</span><b>$0</b></p>
    <p class="box-line" style="margin-top:9px"><b>BUILD YOUR OWN</b><span class="sep">|</span><b>$0</b></p>
  </section>

  <span class="rope" style="left:341px;top:621px;width:260px"></span>

  <ul class="items mid" style="left:377px;top:644px;width:220px">
    <li class="item"><p class="name">Ceviche<span class="price">$0</span></p><p class="desc">Citrus, fruit, peppers, onion, cilantro</p></li>
    <li class="item"><p class="name">Tuna Poke/Crudo<span class="price">$0</span></p><p class="desc">Ponzu, scallions, ginger, avocado,<br>sesame</p></li>
    <li class="item"><span class="pick"></span><p class="name">Scallop Crudo<span class="price">$0</span></p><p class="desc">Lemon, ginger, chives, olive oil,<br>pine nuts</p></li>
    <li class="item"><p class="name">Peel &amp; Eat Shrimp<span class="price">$0</span></p><p class="desc">Remoulade, tartar, cocktail</p></li>
    <li class="item"><p class="name">Local Fish Crudo<span class="price">$0</span></p><p class="desc">Seasonal accompaniments</p></li>
    <li class="item"><p class="name">Cured Salmon<span class="price">$0</span></p></li>
  </ul>

  <ul class="items" style="left:670px;top:267px;width:215px">
    <li class="item"><p class="name">Clam Linguini<span class="price">$0</span></p><p class="desc">Local Pasta. Local Bacon, peppers,<br>butter, herbs</p></li>
    <li class="item"><p class="name">Vegetable Gnocchi<span class="price">$0</span></p><p class="desc">Squash, shallots, peas, mushroom,<br>basil, parmesan</p></li>
    <li class="item"><p class="name">Pan Seared Scallop<span class="price">$0</span></p><p class="desc">Curry, cauliflower, carrots, eggplant,<br>Carolina gold rice</p></li>
    <li class="item"><p class="name">Halibut Gumbo<span class="price">$0</span></p><p class="desc">Shrimp, scallions, okra garnish</p></li>
    <li class="item"><p class="name">Grilled Steak<span class="price">$0</span></p><p class="desc">Roasted rainbow carrots, mashed<br>potatoes, ancho demi, chimichurri</p></li>
    <li class="item"><span class="pick"></span><p class="name">Surf &amp; Turf Filet<span class="price">$0</span></p><p class="desc">Asparagus, baby potatoes,<br>bearnaise, demi</p></li>
    <li class="item"><span class="pick"></span><p class="name">Fresh Catch<span class="price">$0</span></p><p class="name">Crab Legs<span class="price">$0</span></p><p class="desc">Butter, cocktail, spicy remoulade</p></li>
    <li class="item"><p class="name">Lowcountry Boil<span class="price">$0</span></p><p class="desc">Shrimp, sausage, corn, potato</p></li>
    <li class="item"><p class="name">Smash Burger<span class="price">$0</span></p><p class="desc">Spicy “thousand Island,” pickles,<br>house cut fries, LTO</p></li>
    <li class="item"><p class="name">Lobster Roll<span class="price">$0</span></p><p class="desc">Lots of Lobstah, scallions, celery,<br>house fries</p></li>
    <li class="item"><p class="name">Fish Sandwich<span class="price">$0</span></p><p class="desc">Double stacked halibut, pickled<br>carrots, Lemon/caper/dill aioli,<br>lettuce, tomato</p></li>
  </ul>

  <span class="rope" style="left:54px;top:1025px;width:835px"></span>

  <section class="band">
    <h3 class="band-head" style="left:31px;top:18px">KIDS MENU</h3>
    <p class="band-text" style="left:174px;top:18px">Chicken tenders / Mac &amp; cheese /<br>Fried Fish / Fried Shrimp</p>
    <h3 class="band-head" style="left:444px;top:18px">DESSERTS</h3>
    <p class="band-text" style="left:588px;top:18px">Chocolate / Raspberry / Blue Berry</p>
  </section>

  <p class="legend"><span class="dot"></span>Restaurant's Recommendation</p>
</main>
</body>
</html>
```